Computer consultant business card

Plimvo Software is a newly started computer consulting company. It's a small one-man company that provides mostly Android applications but also websites in collaboration with designers. I'm running this company on the side of full time university studies.

I want the final design to be clean and memorable. Be creative! :)

Some inspiration:
http://www.artfenwick.com/design/62242
http://www.artfenwick.com/design/1628455/business-card-design-by-brusqlin
http://www.artfenwick.com/design/918507/business-card-design-by-velinora-quathbridge

See attachment for my company logo.
Updates

I would like to thank everyone for submitting! I'll need a couple of days to review and ultimately select a design.

Target Market(s)

Non-technical entrepreneurs and small companies.

Industry/Entity Type

University

Requirements
Must have
• My company logo.
In any way, both colors from my logo.
First- and last name, e-mail and phone number.
Double-sided design.
Nice to have
• Something creative with the symbol in my logo

```html
<!DOCTYPE html>
<html lang="en">
<head>
<meta charset="utf-8">
<title>Plimvo Software – Business Card</title>
<link rel="stylesheet" href="https://fonts.googleapis.com/css2?family=Exo+2:wght@300;400&display=swap">
<style>
  :root {
    --page: #e6e4e0;
    --card-dark: #121212;
    --card-dark-mid: #2a2a2a;
    --card-dark-soft: #1d1d1d;
    --card-light: #f4f4f4;
    --brand-blue: #4a7fcf;
    --brand-grey: #4a4a4a;
    --text-grey: #5a5a5a;
    --shadow: rgba(0, 0, 0, 0.28);
  }
  * { box-sizing: border-box; margin: 0; padding: 0; }
  html, body {
    width: 1200px;
    height: 1024px;
    overflow: hidden;
    background: var(--page);
    font-family: "Exo 2", "Helvetica Neue", Arial, sans-serif;
  }
  .canvas {
    position: relative;
    width: 1200px;
    height: 1024px;
  }
  .card {
    position: absolute;
    left: 215px;
    width: 770px;
    height: 440px;
    border-radius: 4px;
    box-shadow: 0 14px 34px var(--shadow);
    overflow: hidden;
  }
  .card--front { top: 52px; background: var(--card-dark); }
  .card--back { top: 532px; background: var(--card-light); }

  .front-pattern {
    position: absolute;
    inset: 0;
    background:
      radial-gradient(ellipse at 30% 30%, var(--card-dark-mid) 0%, rgba(42,42,42,0) 55%),
      radial-gradient(ellipse at 75% 80%, var(--card-dark-soft) 0%, rgba(29,29,29,0) 60%),
      linear-gradient(160deg, var(--card-dark-mid) 0%, var(--card-dark) 70%);
  }
  .front-sheen {
    position: absolute;
    inset: 0;
    background: linear-gradient(115deg, rgba(255,255,255,0.06) 0%, rgba(255,255,255,0) 40%, rgba(255,255,255,0.04) 70%, rgba(255,255,255,0) 100%);
  }
  .brand {
    position: absolute;
    left: 190px;
    top: 150px;
    display: flex;
    align-items: center;
    gap: 26px;
  }
  .brand-dot {
    width: 96px;
    height: 96px;
    border-radius: 50%;
    background: var(--brand-blue);
  }
  .brand-name {
    font-weight: 400;
    font-size: 112px;
    line-height: 1;
    letter-spacing: 2px;
    color: var(--brand-grey);
  }
  .front-url {
    position: absolute;
    right: 128px;
    top: 272px;
    font-weight: 300;
    font-size: 26px;
    letter-spacing: 4px;
    color: var(--brand-blue);
  }

  .back-mark {
    position: absolute;
    left: 64px;
    top: 56px;
    width: 34px;
    height: 34px;
    border-radius: 50%;
    background: var(--brand-blue);
  }
  .contact {
    position: absolute;
    left: 64px;
    bottom: 70px;
    font-weight: 300;
    color: var(--text-grey);
  }
  .contact-name {
    font-weight: 400;
    font-size: 42px;
    letter-spacing: 3px;
    color: var(--brand-blue);
    text-transform: uppercase;
  }
  .contact-title {
    font-size: 24px;
    letter-spacing: 2px;
    margin-bottom: 26px;
  }
  .contact-line {
    font-size: 24px;
    letter-spacing: 2px;
    line-height: 1.5;
  }
</style>
</head>
<body>
<main class="canvas">
  <section class="card card--front" aria-label="Card front">
    <div class="front-pattern" role="img" aria-label="Dark charcoal tiled pattern of rounded droplet shapes across the card face"></div>
    <div class="front-sheen"></div>
    <div class="brand">
      <span class="brand-dot"></span>
      <span class="brand-name">plimvo</span>
    </div>
    <p class="front-url">www.plimvo.com.au</p>
  </section>

  <section class="card card--back" aria-label="Card back">
    <span class="back-mark"></span>
    <div class="contact">
      <p class="contact-name">Jory Danem</p>
      <p class="contact-title">Director</p>
      <p class="contact-line">0491 208 613</p>
      <p class="contact-line">jory@plimvo.com.au</p>
    </div>
  </section>
</main>
</body>
</html>
```